Stationary Design for an engineering start-up.

Company name: Lumetra Plank Inc.

Our advanced materials company utilizes a patented process to spray-coat wood surfaces with metal. Metal is sprayed as a super-heated powder and fully conforms to the surface of the wood allowing for a wide range of applications. Metals used are COPPER and BRONZE.

We need a stationary package that includes Business Card, Letter Head, and Envelope.

- After we will submit a contest for a brochure design, so a winning designer will have advantage to take that project as well.

Target Market(s)

Our target market are building and industrial design professionals.

- Architects
- Designers
- Builders

Industry/Entity Type

Engineering

Requirements
Must have
• - All stationary must include our logo (attached)

Sizes:
Business card: Standard 3.5 by 2 inches. Landscape.

Letterhead: 8.5" x 11"

Envelopes:
One standard commercial size #10 (4 1/8" by 9 1/2")
One catalog size envelope (9" by 12")
Assume envelopes are one-sided (front print only)

- Use bleeds where applicable

- Include all fonts used.

File Format:
AI or PSD
** for letterhead please include MSWord template.
Nice to have
• Design style
- Take design style from our logo and attached images.
- Modern, sharp, minimalistic
- Sans fonts
- Don''t be afraid to use color background for business card.
We''re open to ideas of making the business card somehow representative of the product - metal coated wood.

```html
<!DOCTYPE html>
<html lang="en">
<head>
<meta charset="utf-8">
<title>Lumetra Plank Inc. Letterhead</title>
<link rel="stylesheet" href="https://fonts.googleapis.com/css2?family=Arimo:wght@400;700&display=swap">
<style>
  :root {
    --paper: #fafafa;
    --ink: #111111;
    --copper-dark: #9c5f35;
    --copper-mid: #c47c48;
    --copper-light: #e99563;
    --bronze-red: #a24a3c;
    --bronze-gold: #d9c060;
    --gold-light: #e8dda6;
    --gold-mid: #d9c97f;
    --gold-deep: #cdb55c;
  }
  html, body {
    margin: 0;
    padding: 0;
    overflow: hidden;
    background: var(--paper);
  }
  .letterhead {
    position: relative;
    width: 927px;
    height: 1200px;
    background: var(--paper);
    font-family: "Arimo", Arial, sans-serif;
    color: var(--ink);
    overflow: hidden;
  }
  .header-band, .footer-band {
    position: absolute;
    left: 0;
    display: block;
  }
  .header-band { top: 0; }
  .footer-band { top: 1168px; }
  .brand {
    position: absolute;
    left: 43px;
    top: 45px;
    display: flex;
    align-items: center;
    gap: 16px;
  }
  .brand-square {
    width: 34px;
    height: 34px;
    background: var(--ink);
  }
  .brand-name {
    font-size: 50px;
    font-weight: 400;
    letter-spacing: 6px;
    line-height: 1;
    color: var(--ink);
  }
  .contact-lines {
    position: absolute;
    left: 60px;
    top: 150px;
    width: 306px;
    text-align: center;
    font-size: 17.5px;
    line-height: 22px;
  }
  .contact-lines p { margin: 0; }
  .company-address {
    position: absolute;
    left: 632px;
    top: 90px;
    font-size: 17.5px;
    line-height: 22px;
  }
  .company-name {
    margin: 0 0 2px;
    font-size: 21px;
    font-weight: 700;
    line-height: 26px;
  }
  .address-lines {
    margin: 0;
    padding-left: 24px;
    font-style: normal;
  }
</style>
</head>
<body>
<main class="letterhead">
  <svg class="header-band" width="927" height="228" viewBox="0 0 927 228" aria-hidden="true">
    <defs>
      <linearGradient id="copper" x1="0" y1="0" x2="1" y2="0">
        <stop offset="0" stop-color="var(--copper-dark)"/>
        <stop offset="0.35" stop-color="var(--copper-mid)"/>
        <stop offset="0.6" stop-color="var(--copper-light)"/>
        <stop offset="1" stop-color="var(--copper-mid)"/>
      </linearGradient>
      <linearGradient id="bronze" x1="0" y1="0" x2="0" y2="1">
        <stop offset="0" stop-color="var(--bronze-gold)"/>
        <stop offset="0.3" stop-color="var(--bronze-red)"/>
        <stop offset="0.6" stop-color="var(--bronze-gold)"/>
        <stop offset="1" stop-color="var(--gold-deep)"/>
      </linearGradient>
      <linearGradient id="gold" x1="0" y1="0" x2="1" y2="0">
        <stop offset="0" stop-color="var(--gold-light)"/>
        <stop offset="0.5" stop-color="var(--gold-mid)"/>
        <stop offset="1" stop-color="var(--gold-deep)"/>
      </linearGradient>
    </defs>
    <rect width="927" height="228" fill="url(#gold)"/>
    <polygon points="0,0 927,0 927,38 0,159" fill="url(#bronze)"/>
    <polygon points="0,0 590,0 632,77 0,159" fill="url(#copper)"/>
    <line x1="0" y1="159" x2="927" y2="38" stroke="#8f8a5a" stroke-width="1.2"/>
  </svg>

  <div class="brand">
    <span class="brand-square"></span>
    <span class="brand-name">LUMETRA</span>
  </div>

  <div class="contact-lines">
    <p>Tel - 123.456.7890</p>
    <p>Fax - 123.456.7890</p>
    <p>Web - www.lumetraplank.com</p>
  </div>

  <div class="company-address">
    <p class="company-name">Lumetra Plank Inc.</p>
    <address class="address-lines">
      12 Avenue St.<br>
      Sometown<br>
      Province<br>
      1A2 3B4
    </address>
  </div>

  <svg class="footer-band" width="927" height="32" viewBox="0 0 927 32" aria-hidden="true">
    <defs>
      <linearGradient id="copper-foot" x1="0" y1="0" x2="1" y2="0">
        <stop offset="0" stop-color="var(--copper-dark)"/>
        <stop offset="0.6" stop-color="var(--copper-light)"/>
        <stop offset="1" stop-color="var(--copper-mid)"/>
      </linearGradient>
      <linearGradient id="bronze-foot" x1="0" y1="0" x2="1" y2="0">
        <stop offset="0" stop-color="var(--bronze-red)"/>
        <stop offset="0.5" stop-color="var(--bronze-gold)"/>
        <stop offset="1" stop-color="var(--gold-deep)"/>
      </linearGradient>
    </defs>
    <rect width="927" height="32" fill="url(#bronze-foot)"/>
    <polygon points="0,0 590,0 610,32 0,32" fill="url(#copper-foot)"/>
  </svg>
</main>
</body>
</html>
```